Business Card & Stationery
It must INSTANTLY show u exactly what the business is
Project: Business Card & Stationery
Business Card & Stationery -
Creative Brief
Professional
Gavin Pellworth
Managing Director
PO Box 482 Fernhollow Vic 3159
gavin@brindlecheckfix.com.au
www.brindlecheckfix.com.au
Cert No. QRBX 392
Testing & Tagging to ASNZS 3760 Microwave Oven Leakage Testing Safety Switch Testing (RCD) Jobguard Compliance
Gavin Pellworth Managing Director Tel: 0427 315 682 Brindle Check & Fix Pty Ltd PO Box 482 Fernhollow Vic 3159 Email: gavin@brindlecheckfix.com.au Website: www.brindlecheckfix.com.au

```html
<!DOCTYPE html>
<html lang="en">
<head>
<meta charset="utf-8">
<title>Brindle Check &amp; Fix – Business Card</title>
<link href="https://fonts.googleapis.com/css2?family=Open+Sans:wght@400;600;700;800&display=swap" rel="stylesheet">
<style>
  :root{
    --bg:#2b2b2d;
    --orange:#f07a14;
    --orange-light:#fba84a;
    --orange-deep:#e0600a;
    --ink:#222222;
    --ink-soft:#3a3a3a;
    --shade:#4a4a4a;
    --paper:#ffffff;
  }
  *{box-sizing:border-box;margin:0;padding:0}
  html,body{width:1200px;height:852px;overflow:hidden;background:var(--bg)}
  body{position:relative;font-family:"Open Sans",Arial,sans-serif;color:var(--ink)}
  .card{position:absolute;width:560px;height:320px;border-radius:18px;background:var(--paper);overflow:hidden;box-shadow:0 10px 28px rgba(0,0,0,.45)}
  .card--back{left:60px;top:70px}
  .card--front{left:580px;top:462px}
  .card svg.wave{position:absolute;inset:0;width:100%;height:100%}
  .details{position:absolute;font-size:11.5px;line-height:1.45;color:var(--ink-soft)}
  .person .name{font-weight:700;font-size:17px;color:var(--ink);line-height:1.2}
  .person .role{font-weight:600;font-size:12px;color:var(--ink)}
  .licence{margin-top:68px}
  .address{margin-top:14px}
  .contacts{margin-top:14px;list-style:none}
  .contacts li{display:flex;align-items:center;gap:8px;height:18px}
  .contacts svg{width:12px;height:12px;flex:none}
  .card--back .details{left:26px;top:38px;width:240px}
  .card--front .details{right:22px;top:40px;width:230px;text-align:right}
  .card--front .contacts li{flex-direction:row-reverse;justify-content:flex-start}
  .wordmark{position:absolute;display:flex;align-items:center;gap:8px;font-weight:800;font-size:22px;color:var(--orange);white-space:nowrap}
  .wordmark .dot{width:12px;height:12px;border-radius:50%;background:var(--ink);flex:none}
  .card--back .wordmark{left:300px;top:102px}
  .card--front .wordmark{left:30px;top:100px}
</style>
</head>
<body>

<section class="card card--back" aria-label="Business card, contact side">
  <svg class="wave" viewBox="0 0 560 320" preserveAspectRatio="none">
    <defs>
      <linearGradient id="orangeA" x1="0" y1="0" x2="1" y2="1">
        <stop offset="0" stop-color="var(--orange-deep)"/>
        <stop offset=".55" stop-color="var(--orange-light)"/>
        <stop offset="1" stop-color="var(--orange)"/>
      </linearGradient>
    </defs>
    <path d="M0 0H270C205 50 285 150 240 220C215 262 228 300 246 320H0Z" fill="var(--shade)" transform="translate(10 0)"/>
    <path d="M0 0H270C205 50 285 150 240 220C215 262 228 300 246 320H0Z" fill="url(#orangeA)"/>
  </svg>
  <div class="details">
    <div class="person">
      <p class="name">Gavin Pellworth</p>
      <p class="role">Managing Director</p>
    </div>
    <p class="licence">License No. QRBX 392</p>
    <p class="address">PO Box 482<br>Fernhollow Vic 3159</p>
    <ul class="contacts">
      <li><svg viewBox="0 0 12 12"><path d="M3 1L5 3.5 4 5C5 7 6 8 7 8.5L8.5 7.5 11 9.5 10 11C5 11 1 7 1 2Z" fill="var(--ink)"/></svg>0427 315 682</li>
      <li><svg viewBox="0 0 12 12"><rect x="1" y="2.5" width="10" height="7" rx="1" fill="var(--ink)"/><path d="M1.5 3L6 6.5 10.5 3" stroke="#fff" fill="none"/></svg>gavin@brindlecheckfix.com.au</li>
      <li><svg viewBox="0 0 12 12"><circle cx="6" cy="6" r="4.8" fill="none" stroke="var(--ink)" stroke-width="1.2"/><path d="M1.5 6H10.5M6 1.2C3.5 4 3.5 8 6 10.8M6 1.2C8.5 4 8.5 8 6 10.8" stroke="var(--ink)" fill="none" stroke-width=".9"/></svg>www.brindlecheckfix.com.au</li>
    </ul>
  </div>
  <p class="wordmark"><span class="dot"></span>Brindle Check &amp; Fix</p>
</section>

<section class="card card--front" aria-label="Business card, logo side">
  <svg class="wave" viewBox="0 0 560 320" preserveAspectRatio="none">
    <defs>
      <linearGradient id="orangeB" x1="1" y1="0" x2="0" y2="1">
        <stop offset="0" stop-color="var(--orange-deep)"/>
        <stop offset=".5" stop-color="var(--orange-light)"/>
        <stop offset="1" stop-color="var(--orange)"/>
      </linearGradient>
    </defs>
    <path d="M560 0H300C372 40 292 150 330 220C352 262 338 300 318 320H560Z" fill="var(--shade)" transform="translate(-10 0)"/>
    <path d="M560 0H300C372 40 292 150 330 220C352 262 338 300 318 320H560Z" fill="url(#orangeB)"/>
  </svg>
  <p class="wordmark"><span class="dot"></span>Brindle Check &amp; Fix</p>
  <div class="details">
    <div class="person">
      <p class="name">Gavin Pellworth</p>
      <p class="role">Managing Director</p>
    </div>
    <p class="licence">License No. QRBX 392</p>
    <p class="address">PO Box 482<br>Fernhollow Vic 3159</p>
    <ul class="contacts">
      <li><svg viewBox="0 0 12 12"><path d="M3 1L5 3.5 4 5C5 7 6 8 7 8.5L8.5 7.5 11 9.5 10 11C5 11 1 7 1 2Z" fill="var(--ink)"/></svg>0427 315 682</li>
      <li><svg viewBox="0 0 12 12"><rect x="1" y="2.5" width="10" height="7" rx="1" fill="var(--ink)"/><path d="M1.5 3L6 6.5 10.5 3" stroke="#fff" fill="none"/></svg>gavin@brindlecheckfix.com.au</li>
      <li><svg viewBox="0 0 12 12"><circle cx="6" cy="6" r="4.8" fill="none" stroke="var(--ink)" stroke-width="1.2"/><path d="M1.5 6H10.5M6 1.2C3.5 4 3.5 8 6 10.8M6 1.2C8.5 4 8.5 8 6 10.8" stroke="var(--ink)" fill="none" stroke-width=".9"/></svg>www.brindlecheckfix.com.au</li>
    </ul>
  </div>
</section>

</body>
</html>
```